Acai Label - 2oz

I'm going to need a graphic label for 2oz Amble Glass bottle. My company is Brisk Harbor and this particular product is an energy shot. (organic). Please see attachments for example.
Dimensions of Bottle - I need a full wrap concept
Color: Amber
Size: 2 oz
Material: Glass
Case Pack: 240
Neck finish: 20-400
Height: 3.687 in / 9.365 cm
Diameter: 1.52 in / 3.861 cm
Label Dimensions: 4.625 x 1.75 in
Print Dimensions: 4.75 x 1.75 in
Please incorporate existing Brisk Harbor Logo on label.
Target Market(s)
Target market is - people that are interested natural forms of an energy boost.
Ages from 16- 40. I'd like it to appeal to broad spectrum of people. Please submit all creative designs and refinement can always come after.
Industry/Entity Type
It Company

```html
<!DOCTYPE html>
<html lang="en">
<head>
<meta charset="utf-8">
<title>Brisk Harbor Organic Energy – Acai Label</title>
<link href="https://fonts.googleapis.com/css2?family=Oswald:wght@500;600;700&family=Roboto:wght@700&display=swap" rel="stylesheet">
<style>
  :root {
    --bg-top: #ffffff;
    --bg-bottom: #ececec;
    --label-green: #3fa83a;
    --label-green-light: #8fcb4f;
    --label-green-dark: #2e8f31;
    --berry-maroon: #8a2636;
    --berry-deep: #5e1524;
    --cap-purple: #7b3f97;
    --cap-purple-light: #b07ac8;
    --cap-purple-dark: #5a2a72;
    --headline-outline: #8c1f5c;
    --banner-pink: #e0147a;
    --acai-purple: #5b2b8a;
    --text-white: #ffffff;
    --seal: #ffffff;
  }
  html, body {
    margin: 0;
    padding: 0;
    width: 1200px;
    height: 1200px;
    overflow: hidden;
  }
  body {
    background: linear-gradient(180deg, var(--bg-top) 0%, var(--bg-top) 60%, var(--bg-bottom) 100%);
  }
  .label-sheet {
    display: block;
    width: 1200px;
    height: 1200px;
  }
  .brand-name {
    font-family: "Oswald", sans-serif;
    font-weight: 500;
    fill: var(--text-white);
  }
  .headline {
    font-family: "Oswald", sans-serif;
    font-weight: 600;
    fill: var(--text-white);
    stroke: var(--headline-outline);
    stroke-width: 10;
    stroke-linejoin: round;
    paint-order: stroke;
  }
  .flavor-banner-text {
    font-family: "Oswald", sans-serif;
    font-weight: 600;
    fill: var(--text-white);
  }
  .flavor-name {
    font-family: "Oswald", sans-serif;
    font-weight: 600;
    fill: var(--acai-purple);
  }
  .claim-main {
    font-family: "Oswald", sans-serif;
    font-weight: 600;
    fill: var(--text-white);
  }
  .claim-sub {
    font-family: "Oswald", sans-serif;
    font-weight: 500;
    fill: var(--text-white);
  }
  .volume {
    font-family: "Roboto", sans-serif;
    font-weight: 700;
    fill: var(--text-white);
  }
</style>
</head>
<body>
<svg class="label-sheet" viewBox="0 0 1200 1200" xmlns="http://www.w3.org/2000/svg">
  <defs>
    <radialGradient id="labelGreen" cx="50%" cy="62%" r="60%">
      <stop offset="0%" stop-color="var(--label-green-light)"/>
      <stop offset="60%" stop-color="var(--label-green)"/>
      <stop offset="100%" stop-color="var(--label-green-dark)"/>
    </radialGradient>
    <linearGradient id="baseBand" x1="0" y1="0" x2="0" y2="1">
      <stop offset="0%" stop-color="var(--berry-maroon)"/>
      <stop offset="100%" stop-color="var(--berry-deep)"/>
    </linearGradient>
    <linearGradient id="capShade" x1="0" y1="0" x2="0" y2="1">
      <stop offset="0%" stop-color="var(--cap-purple-light)"/>
      <stop offset="35%" stop-color="var(--cap-purple)"/>
      <stop offset="100%" stop-color="var(--cap-purple-dark)"/>
    </linearGradient>
    <radialGradient id="berryTones" cx="50%" cy="50%" r="55%">
      <stop offset="0%" stop-color="#4a2a48"/>
      <stop offset="70%" stop-color="#1c1422"/>
      <stop offset="100%" stop-color="#0f0b12"/>
    </radialGradient>
    <radialGradient id="berryLeafTones" cx="50%" cy="50%" r="55%">
      <stop offset="0%" stop-color="#3a1a30"/>
      <stop offset="55%" stop-color="#4f7a3a"/>
      <stop offset="100%" stop-color="#6fb048" stop-opacity="0"/>
    </radialGradient>
    <clipPath id="bottleBody">
      <path d="M-118,190 C-118,250 -190,270 -190,370 L-190,1130 Q-190,1170 -150,1170 L150,1170 Q190,1170 190,1130 L190,370 C190,270 118,250 118,190 Z"/>
    </clipPath>
    <clipPath id="photoWindow">
      <circle cx="-17" cy="828" r="118"/>
    </clipPath>
  </defs>

  <!-- Bottle: bowl flavor view -->
  <g class="bottle bottle--bowl" transform="translate(343 0)">
    <g class="bottle-body" clip-path="url(#bottleBody)">
      <rect x="-200" y="180" width="400" height="1000" fill="url(#labelGreen)"/>
      <rect class="base-band" x="-200" y="1005" width="400" height="175" fill="url(#baseBand)"/>
    </g>
    <rect class="bottle-cap" x="-130" y="54" width="260" height="140" rx="22" fill="url(#capShade)"/>

    <text class="brand-name" x="0" y="438" text-anchor="middle" font-size="36">Brisk Harbor</text>

    <text class="headline" x="0" y="570" text-anchor="middle" font-size="100" textLength="292" lengthAdjust="spacingAndGlyphs">ORGANIC</text>
    <text class="headline" x="0" y="662" text-anchor="middle" font-size="100" textLength="264" lengthAdjust="spacingAndGlyphs">ENERGY</text>

    <circle class="photo-frame" cx="-17" cy="828" r="130" fill="var(--text-white)"/>
    <rect class="acai-photo" x="-135" y="710" width="236" height="236" clip-path="url(#photoWindow)" fill="url(#berryTones)" role="img" aria-label="Close-up photo of a bowl of dark purple acai berries"/>

    <rect class="flavor-banner" x="-161" y="900" width="295" height="48" fill="var(--banner-pink)"/>
    <text class="flavor-banner-text" x="-13" y="938" text-anchor="middle" font-size="36">ACAI</text>

    <text class="claim-main" x="0" y="1044" text-anchor="middle" font-size="44" textLength="196" lengthAdjust="spacingAndGlyphs">ALL NATURAL</text>
    <text class="claim-sub" x="0" y="1066" text-anchor="middle" font-size="17" textLength="198" lengthAdjust="spacingAndGlyphs">ZERO CALORIES- SUGAR FREE</text>
    <text class="volume" x="0" y="1112" text-anchor="middle" font-size="32" textLength="216" lengthAdjust="spacingAndGlyphs">2 OZ (59ML)</text>

    <circle class="certification-seal" cx="148" cy="1020" r="30" fill="var(--seal)"/>
  </g>

  <!-- Bottle: loose berry view -->
  <g class="bottle bottle--loose" transform="translate(922 0)">
    <g class="bottle-body" clip-path="url(#bottleBody)">
      <rect x="-200" y="180" width="400" height="1000" fill="url(#labelGreen)"/>
      <rect class="base-band" x="-200" y="1005" width="400" height="175" fill="url(#baseBand)"/>
      <ellipse class="acai-photo" cx="-28" cy="846" rx="175" ry="100" fill="url(#berryLeafTones)" role="img" aria-label="Photo of three acai berries with green leaves"/>
    </g>
    <rect class="bottle-cap" x="-130" y="54" width="260" height="140" rx="22" fill="url(#capShade)"/>

    <text class="brand-name" x="0" y="438" text-anchor="middle" font-size="36">Brisk Harbor</text>

    <text class="headline" x="0" y="570" text-anchor="middle" font-size="100" textLength="292" lengthAdjust="spacingAndGlyphs">ORGANIC</text>
    <text class="headline" x="0" y="662" text-anchor="middle" font-size="100" textLength="264" lengthAdjust="spacingAndGlyphs">ENERGY</text>

    <text class="flavor-name" x="0" y="996" text-anchor="middle" font-size="40">ACAI</text>

    <text class="claim-main" x="0" y="1044" text-anchor="middle" font-size="44" textLength="196" lengthAdjust="spacingAndGlyphs">ALL NATURAL</text>
    <text class="claim-sub" x="0" y="1066" text-anchor="middle" font-size="17" textLength="198" lengthAdjust="spacingAndGlyphs">ZERO CALORIES- SUGAR FREE</text>
    <text class="volume" x="0" y="1112" text-anchor="middle" font-size="32" textLength="216" lengthAdjust="spacingAndGlyphs">2 OZ (59ML)</text>

    <circle class="certification-seal" cx="148" cy="1020" r="30" fill="var(--seal)"/>
  </g>
</svg>
</body>
</html>
```